Banner Design for Brisk Loans

Hi,

I know this is under flyer design, however, I am actually after a Banner (I could not find this option). The banner needs to be done to fit the following specifications.

1 x 850mm W x 1500mm H Double Sided Luxury Retractable

I have provided a banner which I currently have however, I would like it to be updated.

I would like to banners created.

Banner 1

The banner should still maintain the lender logos and the fact we assess over 30 lenders, plus also promote the 'Brisk Loans' logo.

Along with this is I would like to promote the 'Brisk Cost Refund.'

Also have the wording
'We Cover your Discharge fee and new loan application fee'
also may use this link as guidance http://www.briskloansdemo.com.au/briskrefund/

Banner 2

This banner I would like it to promote a 'Quick Mortgage Health Check'.

Also include 'The Brisk Loans Edge'

http://www.briskloansdemo.com.au/briskrefund/

Again use this as a guide as to the 4 points of difference, you may use different icons if you feel it looks better

Target Market(s)

People with Home Loans

Industry/Entity Type

Finance

Font styles to use
Sans Serif

Colors
ec1f27
ffffff

Requirements
Must have
• As per the description
Nice to have
• Professional look, good icons to accompany wording
Should not have
• unprofessional look too much text or cluttered

```html
<!DOCTYPE html>
<html lang="en">
<head>
<meta charset="utf-8">
<title>Brisk Loans – Brisk Cost Refund Banner</title>
<link rel="stylesheet" href="https://fonts.googleapis.com/css2?family=Open+Sans:wght@400;600;700;800&family=Montserrat:wght@600&family=Libre+Baskerville:wght@700&display=swap">
<style>
  :root {
    --brand-red: #ec1f27;
    --room-top: #b3121a;
    --room-mid: #8f0c12;
    --room-low: #c51a22;
    --white: #ffffff;
    --ink: #1d1d1d;
    --lender-ink: #3a3a3a;
    --rule: #c9c9c9;
    --frame-line: #d8d8d8;
  }
  * { margin: 0; padding: 0; box-sizing: border-box; }
  html, body { width: 706px; height: 1200px; overflow: hidden; background: var(--white); }
  .banner {
    position: relative; width: 706px; height: 1200px;
    font-family: "Open Sans", Arial, sans-serif; color: var(--ink);
  }
  .frame {
    position: absolute; left: 30px; top: 30px; width: 646px; height: 1140px;
    border: 1px solid var(--frame-line); overflow: hidden; background: var(--white);
  }
  .artwork { position: absolute; left: 0; top: 0; }
  .brand {
    position: absolute; left: 0; right: 0; top: 150px; text-align: center;
  }
  .brand-name {
    font-weight: 700; font-size: 48px; letter-spacing: 1px;
    color: var(--brand-red); line-height: 1;
  }
  .brand-mark {
    display: inline-block; width: 24px; height: 24px; background: var(--brand-red);
    margin-right: 14px; vertical-align: 4px;
  }
  .tagline {
    margin-top: 16px; font-family: "Libre Baskerville", Georgia, serif;
    font-weight: 700; font-size: 12.5px; letter-spacing: .3px; color: var(--ink);
  }
  .offer-title {
    position: absolute; right: 140px; top: 418px; text-align: right;
    color: var(--white); font-weight: 800; line-height: 1.15;
  }
  .offer-title span { display: block; font-size: 46px; }
  .offer-band {
    position: absolute; left: 0; top: 666px; width: 646px; height: 118px;
    background: var(--brand-red); color: var(--white); text-align: center;
    font-weight: 700; padding-top: 20px;
  }
  .offer-band .line-1 { font-size: 34px; line-height: 44px; }
  .offer-band .line-2 { font-size: 29px; line-height: 40px; }
  .lenders {
    position: absolute; left: 26px; top: 834px; width: 580px; height: 248px;
    border: 1px solid var(--rule); border-bottom: none;
  }
  .lenders-label {
    position: absolute; left: 88px; top: -24px; width: 404px; height: 46px;
    background: var(--white); border: 1px solid #bdbdbd; border-radius: 5px;
    font-family: "Montserrat", Arial, sans-serif; font-weight: 600;
    font-size: 24px; letter-spacing: .8px; line-height: 44px; text-align: center;
  }
  .lender-grid {
    position: absolute; left: 12px; right: 12px; top: 52px;
    display: grid; grid-template-columns: repeat(5, 1fr); row-gap: 28px;
    align-items: center; justify-items: center;
  }
  .lender {
    height: 40px; display: flex; align-items: center; justify-content: center;
    font-weight: 700; font-size: 15px; line-height: 1.15; text-align: center;
    color: var(--lender-ink);
  }
  .footer-band {
    position: absolute; left: 0; top: 1082px; width: 646px; height: 58px;
    background: var(--brand-red); color: var(--white); text-align: center;
    font-weight: 700; font-size: 30px; line-height: 58px;
  }
</style>
</head>
<body>
<div class="banner">
  <div class="frame">
    <svg class="artwork" width="646" height="666" viewBox="0 0 646 666">
      <defs>
        <linearGradient id="roomTone" x1="0" y1="0" x2="0" y2="1">
          <stop offset="0" stop-color="var(--room-top)"/>
          <stop offset=".55" stop-color="var(--room-mid)"/>
          <stop offset="1" stop-color="var(--room-low)"/>
        </linearGradient>
      </defs>
      <polygon points="0,0 212,0 0,66" fill="var(--brand-red)"/>
      <rect x="0" y="226" width="646" height="440" fill="url(#roomTone)" role="img" aria-label="Photo of a red-toned living room with sofas and a hand pointing upward"/>
      <polygon points="0,226 646,226 0,366" fill="var(--white)"/>
      <polygon points="0,366 646,226 646,262 0,372" fill="var(--brand-red)"/>
      <rect x="22" y="370" width="592" height="188" fill="var(--brand-red)" opacity=".55"/>
      <path d="M 418 552 A 128 128 0 1 0 336 420" fill="none" stroke="var(--white)" stroke-width="9"/>
      <polygon points="310,406 368,386 346,438" fill="var(--white)"/>
    </svg>

    <div class="brand">
      <div class="brand-name"><span class="brand-mark"></span>Brisk Loans</div>
      <div class="tagline">IS YOUR HOME LOAN WORKING FOR YOU?</div>
    </div>

    <h1 class="offer-title"><span>BRISK COST</span><span>REFUND</span></h1>

    <div class="offer-band">
      <div class="line-1">WE COVER YOUR DISCHARGE FEE</div>
      <div class="line-2">AND NEW LOAN APPLICATION FEE</div>
    </div>

    <section class="lenders">
      <h2 class="lenders-label">We Assess Over 30 Lenders</h2>
      <div class="lender-grid">
        <div class="lender">Kestrel Bank</div>
        <div class="lender">Oakfield Finance</div>
        <div class="lender">Mariner Bank</div>
        <div class="lender">Tideway Bank</div>
        <div class="lender">Redgum Bank</div>

        <div class="lender">Lakeshore Mutual</div>
        <div class="lender">Granite Bank</div>
        <div class="lender">Keystone Loans</div>
        <div class="lender">Brightwater</div>
        <div class="lender">Pinnacle Lending</div>

        <div class="lender">Southcross Bank</div>
        <div class="lender">Larkspur Bank</div>
        <div class="lender">Harbour Credit</div>
        <div class="lender">Ironbark</div>
        <div class="lender">Meridian Bank</div>
      </div>
    </section>

    <div class="footer-band">www.briskloansdemo.com.au</div>
  </div>
</div>
</body>
</html>
```